Connected Building Infrastructure Business needs awesome document templates.

We'd like to have a fresh set of document templates for business letters, documents, and power point presentations. Tamarind Wiring and Safety works with IT teams, construction firms, and consultants to provide structured cabling, electronic security, and connected building infrastructure services to firms through the state of New York, Massachusetts, and Vermont.

We have recently refreshed our logo and have started some branding and would like to continue the themes already in place. As a result of this project we are looking for

-letter head template
-document template for sales material (contracts and proposals)
-document template for customer documentation and hand outs
-PowerPoint template for customer and internal presentations

Target Market(s)

CIOs, Vice President of IT Facilities, and Security, Small/Medium Size Business Owners, General Contractors

Industry/Entity Type

Business

Font styles to use
Sans Serif

Requirements
Must have
• -letter head template
• -document template for sales material (contracts and proposals)
• -document template for customer documentation and hand outs
• -PowerPoint template for customer and internal presentations
Should not have
• Do not change logo. Can use knockout and/or black and white version of logo if needed.

```html
<!DOCTYPE html>
<html lang="en">
<head>
<meta charset="utf-8">
<title>Tamarind Wiring and Safety — Letterhead</title>
<link href="https://fonts.googleapis.com/css2?family=Montserrat:wght@600;700&family=Source+Sans+3:wght@400;600&display=swap" rel="stylesheet">
<style>
  :root {
    --bg-green: #075c3d;
    --brand-green: #0b6a43;
    --brand-dark: #1c1c1c;
    --bar-grey: #616161;
    --text: #2e2e2e;
    --paper: #ffffff;
    --faint: #ededed;
    --badge: #d5d8d7;
  }
  * { margin: 0; padding: 0; box-sizing: border-box; }
  html, body { width: 1200px; height: 706px; overflow: hidden; }
  body { background: var(--bg-green); position: relative; font-family: "Source Sans 3", Arial, sans-serif; }

  .sheet {
    position: absolute; top: 44px; width: 439px; height: 620px;
    background: var(--paper); box-shadow: 0 2px 6px rgba(0,0,0,.35); overflow: hidden;
  }
  .sheet--letter { left: 151px; }
  .sheet--cover { left: 650px; }

  .footer-band { position: absolute; bottom: 0; height: 8px; }
  .footer-band--green { left: 0; width: 257px; background: var(--brand-green); }
  .footer-band--grey { left: 257px; right: 0; background: var(--bar-grey); }

  .header-block { position: absolute; top: 40px; left: 0; width: 46px; height: 46px; background: var(--brand-green); }

  .brand { position: absolute; text-align: center; font-family: "Montserrat", Arial, sans-serif; font-weight: 700; color: var(--brand-dark); }
  .brand__mark { display: block; margin: 0 auto; background: var(--brand-green); }
  .brand__name { display: block; line-height: 1.05; }

  .brand--header { left: 54px; top: 20px; width: 90px; }
  .brand--header .brand__mark { width: 24px; height: 24px; margin-bottom: 10px; }
  .brand--header .brand__name--primary { font-size: 11px; letter-spacing: .3px; }
  .brand--header .brand__name--secondary { font-size: 5.6px; }

  .contact-panel {
    position: absolute; top: 40px; left: 257px; width: 182px; height: 46px;
    background: var(--bar-grey); color: #fff; display: flex; padding: 6px 0 0 20px;
    font-size: 5.2px; line-height: 1.3;
  }
  .contact-panel__company { font-family: "Montserrat", Arial, sans-serif; font-weight: 600; font-size: 5.4px; font-variant: small-caps; margin-bottom: 3px; }
  .contact-panel__address { width: 60px; padding-right: 6px; border-right: 0.6px solid rgba(255,255,255,.7); height: 30px; }
  .contact-panel__list { list-style: none; padding: 14px 0 0 8px; }
  .contact-panel__list li { display: flex; align-items: center; gap: 5px; }
  .contact-panel__icon { width: 4px; height: 4px; border-radius: 1px; background: #fff; }

  .letter-text { position: absolute; left: 47px; width: 350px; font-size: 8.4px; line-height: 10.6px; color: var(--text); }

  .watermark {
    position: absolute; left: 190px; top: 470px; font-family: "Montserrat", Arial, sans-serif;
    font-weight: 700; font-size: 40px; color: var(--faint); letter-spacing: 1px;
  }
  .signature { position: absolute; left: 301px; top: 478px; width: 88px; height: 54px; background: rgba(0,0,0,.05); border-radius: 4px; }

  .brand--cover { left: 0; width: 100%; top: 235px; }
  .brand--cover .brand__mark { width: 74px; height: 74px; margin-bottom: 40px; }
  .brand--cover .brand__name--primary { font-size: 27px; letter-spacing: 1px; }
  .brand--cover .brand__name--secondary { font-size: 15px; margin-top: 3px; }

  .partner-grid {
    position: absolute; left: 45px; top: 560px; width: 354px;
    display: grid; grid-template-columns: repeat(6, 1fr); gap: 10px 8px;
  }
  .partner-grid__badge { height: 15px; background: var(--badge); border-radius: 2px; }
</style>
</head>
<body>

<section class="sheet sheet--letter">
  <div class="header-block"></div>
  <div class="brand brand--header">
    <span class="brand__mark"></span>
    <span class="brand__name brand__name--primary">TAMARIND</span>
    <span class="brand__name brand__name--secondary">WIRING AND SAFETY</span>
  </div>

  <div class="contact-panel">
    <div class="contact-panel__address">
      <div class="contact-panel__company">Tamarind Wiring<br>and Safety</div>
      42 Birch Ln.<br>Albany, NY 12206
    </div>
    <ul class="contact-panel__list">
      <li><span class="contact-panel__icon"></span>(518) 555-0172</li>
      <li><span class="contact-panel__icon"></span>info@tamarindwiring.com</li>
      <li><span class="contact-panel__icon"></span>www.tamarindwiring.com</li>
    </ul>
  </div>

  <div class="watermark" aria-hidden="true">TAMARIND</div>

  <p class="letter-text" style="top:156px">1420, Maple Grove Street<br>Denver, CO 80203.</p>
  <p class="letter-text" style="top:188px">January 29th, 2011</p>
  <p class="letter-text" style="top:209px">Mr. Harlow<br>President, Harlow Community Center<br>218 Eastern Lane<br>Boston, MA 02108</p>
  <p class="letter-text" style="top:262px">Dear Mr. Harlow:</p>
  <p class="letter-text" style="top:283px">In the first paragraph, one needs to give a brief introduction of oneself. One should also give reference to the purpose of the letter in brief.The second paragraph needs to give the details of the letter and its need. This paragraph is mostly longer than the others and plays the main role in the letter. Keep the sentences short and to the point. Avoid using complex words and sentences.</p>
  <p class="letter-text" style="top:358px">The third and last paragraph is the conclusion of the letter and can be kept short.</p>
  <p class="letter-text" style="top:378px">Sincerely,</p>
  <p class="letter-text" style="top:399px">(this is where the signature of the writer will be placed)</p>
  <p class="letter-text" style="top:421px">Dana Whitcombe<br>Read more at Letterwise: http://www.letterwise.com/articles/professional-letter-format-example.html</p>

  <div class="signature" role="img" aria-label="Handwritten signature of the letter writer"></div>

  <div class="footer-band footer-band--green"></div>
  <div class="footer-band footer-band--grey"></div>
</section>

<section class="sheet sheet--cover">
  <div class="brand brand--cover">
    <span class="brand__mark"></span>
    <span class="brand__name brand__name--primary">TAMARIND</span>
    <span class="brand__name brand__name--secondary">WIRING AND SAFETY</span>
  </div>

  <div class="partner-grid" aria-label="Partner badges">
    <span class="partner-grid__badge"></span><span class="partner-grid__badge"></span><span class="partner-grid__badge"></span>
    <span class="partner-grid__badge"></span><span class="partner-grid__badge"></span><span class="partner-grid__badge"></span>
    <span class="partner-grid__badge"></span><span class="partner-grid__badge"></span><span class="partner-grid__badge"></span>
    <span class="partner-grid__badge"></span><span class="partner-grid__badge"></span><span class="partner-grid__badge"></span>
  </div>

  <div class="footer-band footer-band--green" style="width:310px"></div>
  <div class="footer-band footer-band--grey" style="left:310px"></div>
</section>

</body>
</html>
```